Bref créative
Brochure for Geriatric Clinic
LumaCrest Residence & Geriatric SPA
Trifold (3 panel) brochure to be designed for a healthcare company specialized in assisted living facilities and geriatric rehabilitation.
We want to see the medical, the infrastructure and the nature rich enviroment aspects of our business in the design.
We want the brochure to communicate that our primary goal is to improve the quality of life for the senior and their families.
Specification of the folder
11" x 8.5"
279.4 mm x 215.9 mm
27.9 cm x 21.6 cm
3.7" x 8.5"
93.0 mm x 215.9 mm
9.3 cm x 21.6 cm
Please refer to our website at www.lumacrest-care.example, we provided a google translate menu at the bottom for the designers convenience. All pictures are free to use in this project.
Health
Personal, elderly, seniors an their families
Lumacrest logo
.ai format
LumaCrest document brief for brochure

```html
<!DOCTYPE html>
<html lang="en">
<head>
<meta charset="utf-8">
<title>LumaCrest Residence &amp; Geriatric SPA – Trifold Brochure</title>
<link href="https://fonts.googleapis.com/css2?family=Playfair+Display:ital,wght@0,700;1,600&family=Open+Sans:wght@400;600&display=swap" rel="stylesheet">
<style>
  :root {
    --page-bg: #e9e9ea;
    --paper-light: #f8f3e1;
    --paper-mid: #eee3bf;
    --paper-deep: #e2d4a4;
    --heading: #8a6a26;
    --heading-dark: #5e4616;
    --body-text: #4a3f2a;
    --fold-line: rgba(120, 95, 40, 0.25);
    --photo-warm: #d9c4a4;
    --photo-cool: #b9cfd8;
    --map-base: #f4efdf;
    --accent-red: #c9463d;
  }
  * { box-sizing: border-box; margin: 0; padding: 0; }
  html, body { width: 1200px; height: 799px; overflow: hidden; }
  body {
    background: var(--page-bg);
    font-family: "Open Sans", sans-serif;
    color: var(--body-text);
    display: flex;
    align-items: center;
    justify-content: center;
  }
  .brochure-spread {
    width: 930px;
    height: 719px;
    display: grid;
    grid-template-columns: repeat(3, 1fr);
    background: linear-gradient(160deg, var(--paper-light) 0%, var(--paper-mid) 60%, var(--paper-deep) 100%);
    box-shadow: 0 10px 30px rgba(0,0,0,0.18);
  }
  .panel {
    position: relative;
    padding: 28px 26px;
    display: flex;
    flex-direction: column;
    border-right: 1px solid var(--fold-line);
  }
  .panel:last-child { border-right: none; }
  .section-title {
    font-family: "Playfair Display", serif;
    font-weight: 700;
    font-size: 22px;
    color: var(--heading);
    margin-bottom: 8px;
  }
  .subsection-title {
    font-family: "Playfair Display", serif;
    font-weight: 700;
    font-size: 14px;
    letter-spacing: 1px;
    text-transform: uppercase;
    color: var(--heading-dark);
    margin: 6px 0 6px;
  }
  .body-copy { font-size: 11.5px; line-height: 1.55; }
  .signature {
    font-family: "Playfair Display", serif;
    font-style: italic;
    font-size: 12px;
    color: var(--heading);
    text-align: right;
    margin: 4px 0 16px;
  }
  .service-list { list-style: none; font-size: 11.5px; line-height: 1.7; margin-bottom: 10px; }
  .service-list li::before {
    content: "";
    display: inline-block;
    width: 5px; height: 5px;
    background: var(--heading);
    border-radius: 50%;
    margin: 0 8px 2px 0;
  }
  .photo {
    border-radius: 2px;
    flex-shrink: 0;
  }
  .photo-residents {
    margin: auto -26px -28px;
    height: 170px;
    background: linear-gradient(120deg, var(--photo-warm), #efe6d6 55%, #c9b08a);
  }
  .photo-care {
    margin: -28px -26px 18px;
    height: 165px;
    background: linear-gradient(110deg, var(--photo-cool), #eef1f2 50%, var(--photo-warm));
  }
  .map-area {
    margin: -28px -26px 0;
    height: 470px;
    background: linear-gradient(150deg, var(--map-base), #ebe2c6);
  }
  .brand-block {
    margin-top: auto;
    display: flex;
    align-items: center;
    justify-content: center;
    gap: 12px;
    padding-bottom: 30px;
  }
  .brand-dot {
    width: 46px; height: 46px;
    border-radius: 50%;
    background: var(--heading);
  }
  .brand-name {
    font-family: "Playfair Display", serif;
    font-weight: 700;
    font-size: 30px;
    color: var(--heading);
  }
  .brand-tagline {
    text-align: center;
    font-size: 11px;
    letter-spacing: 1px;
    color: var(--heading-dark);
    margin-top: -22px;
    padding-bottom: 26px;
  }
</style>
</head>
<body>
  <main class="brochure-spread">
    <section class="panel panel-philosophy">
      <h2 class="section-title">Our Philosophy</h2>
      <p class="body-copy">At LumaCrest we believe every senior deserves dignity, comfort and joy. Our caring team works closely with residents and their families to improve quality of life each day, in a calm home surrounded by nature and gardens.</p>
      <p class="signature">— The LumaCrest Team</p>
      <h2 class="section-title">Our Services</h2>
      <h3 class="subsection-title">Nursing Home:</h3>
      <ul class="service-list">
        <li>Round-the-clock nursing care</li>
        <li>Private and shared rooms</li>
        <li>Daily medical supervision</li>
        <li>Physical therapy and rehabilitation</li>
        <li>Medication management</li>
        <li>Nutritious home-style meals</li>
        <li>Memory care programs</li>
        <li>Social and leisure activities</li>
        <li>Garden walks and outings</li>
        <li>Family visiting lounges</li>
      </ul>
      <div class="photo photo-residents" role="img" aria-label="Photo of residents relaxing together in a bright lounge"></div>
    </section>

    <section class="panel panel-care">
      <div class="photo photo-care" role="img" aria-label="Photo of a nurse caring for an elderly woman"></div>
      <ul class="service-list">
        <li>Dementia and Alzheimer care</li>
        <li>Post-surgery recovery</li>
        <li>Respite short stays</li>
        <li>Palliative comfort care</li>
        <li>Hydrotherapy spa</li>
      </ul>
      <h3 class="subsection-title">Optional Services</h3>
      <ul class="service-list">
        <li>Hairdresser and manicure</li>
        <li>Private transport</li>
        <li>Personal laundry</li>
        <li>Podiatry visits</li>
        <li>Dietitian consults</li>
        <li>Music and art therapy</li>
      </ul>
      <h2 class="section-title">Our Location</h2>
      <h3 class="subsection-title">Directions:</h3>
      <p class="body-copy">From the city centre take the main avenue north, turn right after the park and follow the signs to LumaCrest. Free parking is available at the entrance.</p>
    </section>

    <section class="panel panel-map">
      <div class="map-area" role="img" aria-label="Street map showing the route to the residence"></div>
      <div class="brand-block">
        <span class="brand-dot"></span>
        <span class="brand-name">LumaCrest</span>
      </div>
      <p class="brand-tagline">Residence &amp; Geriatric SPA</p>
    </section>
  </main>
</body>
</html>
```